Chiropractor needs a snazzy business card

Business card for a chiropractic office.
Office treats patients of all ages.
Focus is on a natural lifestyle.
Colors can include the logo colors as well as white and a little orange.
Ideally the card would have something chiropractic related such as a spine.

The back of the card should have a items for making appointments (date, times....)

```html
<!DOCTYPE html>
<html lang="en">
<head>
<meta charset="utf-8">
<title>Meridian Chiropractic – Business Card</title>
<link href="https://fonts.googleapis.com/css2?family=Didact+Gothic&display=swap" rel="stylesheet">
<style>
  :root {
    --stage: #e9e9e9;
    --stage-light: #f7f7f7;
    --paper: #f4f4f2;
    --navy: #123c6e;
    --green: #4fa335;
    --ink: #2b2b2b;
    --muted: #8a8a8a;
    --field-line: #d8dae6;
    --field-label: #2a4f80;
    --notes-line: #e4ecdb;
    --spine-dark: #9a9a9a;
    --spine-light: #ecebe8;
  }
  * { box-sizing: border-box; margin: 0; padding: 0; }
  html, body { width: 1200px; height: 1000px; overflow: hidden; }
  body {
    background: radial-gradient(ellipse at 50% 40%, var(--stage-light), var(--stage) 75%);
    font-family: "Didact Gothic", "Century Gothic", sans-serif;
    color: var(--ink);
    position: relative;
  }
  .card {
    position: absolute;
    top: 210px;
    width: 330px;
    height: 580px;
    background: var(--paper);
    box-shadow: 0 10px 28px rgba(0,0,0,0.16);
    overflow: hidden;
  }
  .card--front { left: 240px; }
  .card--back { left: 630px; }

  .spine-art {
    position: absolute;
    left: 0; top: 0;
    width: 100%; height: 370px;
    background:
      radial-gradient(ellipse 22% 46% at 52% 52%, var(--spine-dark), transparent 70%),
      radial-gradient(ellipse 48% 40% at 50% 45%, #d6d5d2, transparent 75%),
      var(--spine-light);
  }

  .brand-bands {
    position: absolute;
    left: 0; width: 100%;
  }
  .brand-bands .band-green { height: 5px; background: var(--green); }
  .brand-bands .band-navy { height: 10px; background: var(--navy); }
  .card--front .brand-bands { top: 370px; }
  .card--back .brand-bands { top: 405px; }

  .contact {
    position: absolute;
    right: 34px; top: 402px;
    text-align: right;
    font-size: 17px;
    line-height: 1.25;
  }

  .brand-name {
    position: absolute;
    right: 30px;
    text-align: right;
    color: var(--navy);
    font-weight: 400;
    line-height: 1;
  }
  .brand-name .brand-main { display: block; font-size: 44px; letter-spacing: 1px; }
  .brand-name .brand-sub { display: block; font-size: 21px; letter-spacing: 3px; margin-top: 4px; }
  .card--front .brand-name { top: 460px; }
  .card--back .brand-name { top: 450px; }

  .appointment-title {
    position: absolute;
    left: 30px; top: 22px;
    font-size: 15px;
    color: var(--muted);
  }
  .field {
    position: absolute;
    left: 30px;
    border: 8px solid var(--field-line);
    border-right-width: 0;
    background: var(--paper);
  }
  .field-label {
    position: absolute;
    left: 18px;
    font-size: 14px;
    color: var(--field-label);
  }
  .field--date { top: 52px; width: 250px; height: 66px; }
  .field--date .field-label { top: 18px; }
  .field--times { top: 126px; width: 270px; height: 66px; }
  .field--times .field-label { top: 18px; }
  .field--notes {
    top: 200px; width: 290px; height: 185px;
    border-color: var(--notes-line);
  }
  .field--notes .field-label { top: 72px; left: 112px; }
</style>
</head>
<body>

  <section class="card card--front" aria-label="Card front">
    <div class="spine-art" role="img" aria-label="Translucent x-ray style illustration of a human skeleton with the spine highlighted in dark grey"></div>
    <div class="brand-bands"><div class="band-green"></div><div class="band-navy"></div></div>
    <p class="contact">phone 555-018-2297<br>e-mail meridian@xx.com</p>
    <p class="brand-name"><span class="brand-main">MERIDIAN</span><span class="brand-sub">CHIROPRACTIC</span></p>
  </section>

  <section class="card card--back" aria-label="Card back">
    <p class="appointment-title">Your next appointment is:</p>
    <div class="field field--date"><span class="field-label">date:</span></div>
    <div class="field field--times"><span class="field-label">times:</span></div>
    <div class="field field--notes"><span class="field-label">notes:</span></div>
    <div class="brand-bands"><div class="band-green"></div><div class="band-navy"></div></div>
    <p class="brand-name"><span class="brand-main">MERIDIAN</span><span class="brand-sub">CHIROPRACTIC</span></p>
  </section>

</body>
</html>
```